Looking for business card/letterhead/email signature

Take existing logo and create full design suite of collateral

Contact Information for Business Card

Use mock details that can be edited by us

Font styles to use
Sans Serif

```html
<!DOCTYPE html>
<html lang="en">
<head>
<meta charset="utf-8">
<title>Corvell Digital – Business Card</title>
<link rel="stylesheet" href="https://fonts.googleapis.com/css2?family=Montserrat:wght@700&family=Open+Sans:wght@400;600&display=swap">
<style>
  :root {
    --backdrop: #2a2d31;
    --brand-navy: #0a4f94;
    --brand-sky: #22aee6;
    --card-white: #ffffff;
    --text-grey: #4a4d52;
    --rule-blue: #2a6db5;
  }
  * { margin: 0; padding: 0; box-sizing: border-box; }
  html, body {
    width: 1200px; height: 900px; overflow: hidden;
    background: var(--backdrop);
  }
  .stage {
    width: 1200px; height: 900px;
    display: flex; align-items: center; justify-content: center; gap: 40px;
  }
  .card {
    width: 540px; height: 309px;
    border-radius: 18px; overflow: hidden;
    background: var(--card-white);
    box-shadow: 0 14px 30px rgba(0,0,0,.45);
  }
  .card svg { display: block; }
  .wordmark { font-family: "Montserrat", sans-serif; font-weight: 700; font-size: 24px; }
  .holder-name { font-family: "Montserrat", sans-serif; font-weight: 700; font-size: 24px; fill: var(--brand-navy); }
  .holder-role { font-family: "Open Sans", sans-serif; font-size: 14px; fill: var(--text-grey); }
  .contact-line { font-family: "Open Sans", sans-serif; font-size: 13.5px; fill: var(--text-grey); }
  .web-address { font-family: "Open Sans", sans-serif; font-size: 12px; letter-spacing: 1px; fill: var(--card-white); }
</style>
</head>
<body>
<main class="stage">

  <!-- Contact side -->
  <section class="card card-contact">
    <svg width="540" height="309" viewBox="0 0 540 309">
      <path class="band-sky" d="M0 0 H352 C300 90 232 200 190 309 H0Z" fill="var(--brand-sky)"/>
      <path class="band-navy" d="M0 0 H318 C268 90 200 200 152 309 H0Z" fill="var(--brand-navy)"/>
      <path class="band-highlight" d="M338 20 C285 110 225 205 178 309" fill="none" stroke="var(--card-white)" stroke-width="2"/>

      <g class="brand-lockup">
        <circle cx="38" cy="120" r="9" fill="var(--card-white)"/>
        <text class="wordmark" x="56" y="128" fill="var(--card-white)">Corvell Digital</text>
      </g>

      <text class="holder-name" x="505" y="78" text-anchor="end">Daniel Reyes</text>
      <text class="holder-role" x="505" y="100" text-anchor="end">Owner</text>

      <line x1="285" y1="140" x2="505" y2="140" stroke="var(--rule-blue)" stroke-width="1"/>

      <text class="contact-line" x="488" y="166" text-anchor="end">18 Marlow Ave. Kenbrook,</text>
      <text class="contact-line" x="488" y="184" text-anchor="end">ON K4R2T6</text>
      <path class="icon-pin" d="M505 165 a6 6 0 1 0 -12 0 c0 5 6 11 6 11 s6 -6 6 -11z M499 167 a2 2 0 1 1 0.01 0z" fill="var(--brand-sky)" fill-rule="evenodd"/>

      <line x1="262" y1="204" x2="505" y2="204" stroke="var(--rule-blue)" stroke-width="1"/>

      <text class="contact-line" x="488" y="234" text-anchor="end">+65 8120 4471</text>
      <path class="icon-phone" d="M494 224 c-2 2 -1 7 3 11 s9 5 11 3 l-3 -3 -2 1 c-2 -1 -4 -3 -5 -5 l1 -2z" fill="var(--brand-sky)"/>

      <text class="contact-line" x="488" y="260" text-anchor="end">team@corvelldigital.com</text>
      <g class="icon-mail">
        <rect x="494" y="251" width="14" height="10" rx="1" fill="var(--brand-sky)"/>
        <path d="M494 252 l7 5 7 -5" fill="none" stroke="var(--card-white)" stroke-width="1.2"/>
      </g>
    </svg>
  </section>

  <!-- Brand side -->
  <section class="card card-brand">
    <svg width="540" height="309" viewBox="0 0 540 309">
      <defs>
        <path id="web-curve" d="M70 150 C150 180 240 235 340 268"/>
      </defs>
      <path class="band-sky" d="M0 70 C140 78 300 228 540 258 V309 H0Z" fill="var(--brand-sky)"/>
      <path class="band-navy" d="M0 92 C130 102 290 248 540 280 V309 H0Z" fill="var(--brand-navy)"/>
      <path class="band-highlight" d="M60 100 C170 125 290 230 480 275" fill="none" stroke="var(--card-white)" stroke-width="2"/>

      <g class="brand-lockup">
        <circle cx="262" cy="112" r="9" fill="var(--brand-navy)"/>
        <text class="wordmark" x="280" y="120" fill="var(--brand-navy)">Corvell Digital</text>
      </g>

      <text class="web-address"><textPath href="#web-curve">www.corvelldigital.com</textPath></text>
    </svg>
  </section>

</main>
</body>
</html>
```